Buchcover-Design für Detoxkur
Vielen lieben Dank für die professionelle Zusammenarbeit, die sich auch im zweiten Projekt erfolgreich bestätigen ließ. Tip Top! Dankeschön!!!!
Zielgruppe
Ich bin Gesundheits- und Ernährungsberater und suche nach einem Buchcover für mein neues Projekt (Taschenbuch und E-Book) Meine Zielgruppe sind Menschen die auf der Suche nach Heilung und mehr Wohlbefinden sind. (Detoxkur-Entschlacken und Entgiften etc....)
Aufgabenstellung
Das Design sollte durch den Titel deutlich auffallen. Vorzugsweise ein dunkler Hintergrund, Titel in großer Schrift. Eingearbeitet etwas Gemüse und Obst, grüner Saft oder auch ein Smoothie, Zitronenwasser, Magen- und Darmtrakt oder ähnlichem. Es darf auch verspielt sein aber dennoch Niveauvoll.
Das Buch einschließlich Titel und Untertitel, sowie Klappentext werden derzeit von einem Lektor bearbeitet, also können diesbezüglich noch leichte Änderungen anfallen die dann anzupassen wären.
Das Buchformat ist 12cm x 19cm. Die Endgültigen Abmaße müssten nach dem Buchindesign noch angepasst werden, wenn die Seitenzahlen feststehen.
Würde gerne den Coverdesigner im Impressum des Buchs erwähnen und Bitte darum um Einverständnis, wenn es auch erwünscht sein sollte!
Derzeitiger Text :
Titel: Morgenlicht - Finde Ruhe durch Wandern und Tagträumen
Untertitel: - Durch Entgiften und Entschlacken das Wohlbefinden steigern, die Darmgesundheit wieder herstellen, das Gewicht reduzieren und die Heilung für Körper und Geist einleiten -
Klappentext: Bist du auf der Suche nach mehr Wohlbefinden und möchtest deine Gesundheit nachhaltig verbessern? Suchst du nach Methoden deinen Körper von Schadstoffen zu befreien, die dich in der Vergangenheit belastet haben? Möglicherweise fragst du dich warum das so ist und was es damit auf sich hat?
Detox, Entschlacken und Entgiften, Diäten und eine gesündere Ernährungsweise ist in aller Munde. Der Grund dafür ist bei zahlreichen Menschen ein mangelndes Wohlbefinden durch zivillisationsbedingte Einflüsse wie Umweltverschmutzungen, Stress und eine unbewusste Ernährungsweise. Diese Faktoren führen zu krankhaften Symptomen, Energie- und Antriebslosigkeit und letztendlich zu den steigenden Zahlen übergewichtiger Menschen in unserer Bevölkerung.
In diesem Ratgeber erfährst du, wie wichtig es ist sich zu entgiften und wie wichtig dafür eine gesunde Ernähru..

```html
<!DOCTYPE html>
<html lang="de">
<head>
<meta charset="utf-8">
<title>Morgenlicht – Buchcover</title>
<link rel="stylesheet" href="https://fonts.googleapis.com/css2?family=Alfa+Slab+One&family=Questrial&family=Dancing+Script:wght@500&display=swap">
<style>
  :root {
    --stage: #e8e8e8;
    --slate-dark: #1c1c1c;
    --slate-mid: #3a3a3a;
    --slate-light: #4a4a4a;
    --white: #ffffff;
    --violet: #94479a;
    --violet-deep: #833c89;
    --apple: #e6e6b8;
    --juice-light: #a9bf6e;
    --juice-mid: #4f7a32;
    --juice-dark: #223d1c;
    --portrait-top: #b9b4ad;
    --portrait-bottom: #3a5f98;
    --sans: "Questrial", "Century Gothic", sans-serif;
    --slab: "Alfa Slab One", Georgia, serif;
    --script: "Dancing Script", cursive;
  }
  * { box-sizing: border-box; margin: 0; padding: 0; }
  html, body { width: 1200px; height: 802px; overflow: hidden; background: var(--stage); }
  .stage { position: relative; width: 1200px; height: 802px; }

  .cover {
    position: absolute; top: 60px; width: 420px; height: 665px; overflow: hidden;
    color: var(--white); font-family: var(--sans);
    background:
      radial-gradient(ellipse at 30% 60%, var(--slate-light) 0%, transparent 55%),
      radial-gradient(ellipse at 80% 20%, var(--slate-mid) 0%, transparent 60%),
      var(--slate-dark);
  }
  .cover--front { left: 60px; }
  .cover--back { left: 665px; }

  .front-title {
    position: absolute; top: 58px; left: 0; width: 100%; text-align: center;
    font-family: var(--slab); font-size: 58px; line-height: 1; letter-spacing: 0.5px;
  }
  .front-subtitle {
    position: absolute; top: 128px; right: 32px; font-size: 12.5px; letter-spacing: 0.2px;
  }
  .hero-photo {
    position: absolute; left: 0; top: 178px; width: 392px; height: 352px;
    border-radius: 0 176px 176px 0;
    background:
      radial-gradient(circle at 62% 32%, var(--apple) 0%, transparent 32%),
      radial-gradient(circle at 30% 40%, var(--juice-light) 0%, transparent 45%),
      linear-gradient(135deg, var(--juice-mid) 0%, var(--juice-dark) 100%);
  }

  .author-block { position: absolute; right: 30px; top: 560px; text-align: right; }
  .author-name { font-size: 18px; letter-spacing: 0.5px; }
  .author-role { font-size: 9.5px; margin-top: 2px; }
  .front-tagline {
    position: absolute; left: 16px; right: 16px; top: 612px;
    font-size: 9.6px; line-height: 1.4; text-align: justify; text-align-last: justify;
  }

  .blurb-panel {
    position: absolute; left: 77px; top: 62px; width: 252px; height: 528px;
    background: var(--violet);
  }
  .author-portrait {
    position: absolute; left: 29px; top: 60px; width: 114px; height: 164px;
    background: linear-gradient(180deg, var(--portrait-top) 0%, #8e8a86 45%, var(--portrait-bottom) 100%);
  }
  .blurb {
    position: absolute; font-size: 9.8px; line-height: 13.8px; text-align: justify; hyphens: auto;
  }
  .blurb--lead { left: 158px; top: 82px; width: 160px; }
  .blurb--body { left: 97px; top: 262px; width: 222px; }
  .blurb--body p + p { margin-top: 13px; }
  .blurb-signature {
    position: absolute; right: 20px; top: 540px; font-family: var(--script); font-size: 22px;
  }

  .spine {
    position: absolute; left: 1085px; top: 60px; width: 42px; height: 665px;
    background: var(--violet-deep); color: var(--white); font-family: var(--sans);
  }
  .spine-subtitle, .spine-title {
    position: absolute; left: 0; width: 42px; writing-mode: vertical-rl; transform: rotate(180deg);
    display: flex; align-items: center; justify-content: center; white-space: nowrap;
  }
  .spine-subtitle { top: 30px; height: 330px; font-size: 12.5px; letter-spacing: 0.4px; }
  .spine-title { top: 380px; height: 225px; font-family: var(--slab); font-size: 27px; }
  .spine-author { position: absolute; left: 0; width: 42px; top: 612px; text-align: center; }
  .spine-author-name { font-size: 9px; line-height: 1.05; }
  .spine-author-role { font-size: 4.5px; line-height: 1.2; margin-top: 2px; }
</style>
</head>
<body>
<main class="stage">

  <section class="cover cover--front" aria-label="Vorderseite">
    <h1 class="front-title">Morgenlicht</h1>
    <p class="front-subtitle">Finde Ruhe durch Wandern und Tagträumen</p>

    <div class="hero-photo" role="img" aria-label="In eine Magenform eingefasstes Foto: grüner Saft im Glas mit Apfel, Limette und Grünkohl"></div>

    <div class="author-block">
      <p class="author-name">Jonas Wendrich</p>
      <p class="author-role">Gesundheits- und Ernährungsberater</p>
    </div>
    <p class="front-tagline">Durch Entgiften und Entschlacken das Wohlbefinden steigern, die Darmgesundheit wieder herstellen, das Gewicht reduzieren und die Heilung für Körper und Geist einleiten.</p>
  </section>

  <section class="cover cover--back" aria-label="Rückseite">
    <div class="blurb-panel"></div>
    <div class="author-portrait" role="img" aria-label="Porträtfoto des Autors"></div>
    <p class="blurb blurb--lead">Bist du auf der Suche nach mehr Wohlbefinden und möchtest deine Gesundheit nachhaltig verbessern? Suchst du nach Methoden deinen Körper von Schadstoffen zu befreien, die dich in der Vergangenheit belastet haben? Möglicherweise fragst du dich warum das so ist und was es damit auf sich hat?</p>
    <div class="blurb blurb--body">
      <p>Detox, Entschlacken und Entgiften, Diäten und eine gesündere Ernährungsweise ist in aller Munde. Der Grund dafür ist bei zahlreichen Menschen ein mangelndes Wohlbefinden durch zivilisationsbedingte Einflüsse wie Umweltverschmutzungen, Stress und eine unbewusste Ernährungsweise. Diese Faktoren führen zu krankhaften Symptomen, Energie- und Antriebslosigkeit und letztendlich zu den steigenden Zahlen übergewichtiger Menschen in unserer Bevölkerung.</p>
      <p>In diesem Ratgeber erfährst du, wie wichtig es ist sich zu entgiften und wie wichtig dafür eine gesunde Ernährungsweise ist. Zusätzlich erfährst du, wie du praktische Heilmethoden anwendest, die die Darmgesundheit wiederherstellen und wie du die Entgiftung in den einzelnen Bereichen des Körpers vorantreibst. Denn Detox ist heutzutage wichtiger denn je!</p>
    </div>
    <p class="blurb-signature">Jonas Wendrich</p>
  </section>

  <aside class="spine" aria-label="Buchrücken">
    <p class="spine-subtitle">Finde Ruhe durch Wandern und Tagträumen</p>
    <p class="spine-title">Morgenlicht</p>
    <div class="spine-author">
      <p class="spine-author-name">Jonas<br>Wendrich</p>
      <p class="spine-author-role">Gesundheits- und<br>Ernährungsberater</p>
    </div>
  </aside>

</main>
</body>
</html>
```